Need Powerpoint masters for my consulting company in privacy (RGPD) and IT

For my newly created consulting company I need powerpoint slides masters.
The company is specialzed in privacy (RGPD) and IT.
The company already has a logo (obtained via Marquelane).
These master slides will be mainly used when presenting reports/analysis to clients.
I'll attach a PNG files of the logo.

```html
<!DOCTYPE html>
<html lang="en">
<head>
<meta charset="utf-8">
<title>Aurelien Morvan Conseil – Slide Masters</title>
<link href="https://fonts.googleapis.com/css2?family=Roboto:wght@300;400;500;700;900&display=swap" rel="stylesheet">
<style>
  :root {
    --page-bg: #c9cacc;
    --slide-bg: #f4f1f1;
    --card-bg: #ffffff;
    --teal: #177f8c;
    --teal-dark: #12707c;
    --navy: #0b2238;
    --ink: #2b2b2b;
    --ink-soft: #3d3d3d;
    --rule: #bdbdbd;
    --white: #ffffff;
  }
  * { margin: 0; padding: 0; box-sizing: border-box; }
  html, body { width: 1200px; height: 3288px; overflow: hidden; }
  body { background: var(--page-bg); font-family: 'Roboto', Arial, sans-serif; color: var(--ink); position: relative; }

  .slide { position: absolute; left: 109px; width: 1002px; height: 563px; background: var(--slide-bg); overflow: hidden; }
  .slide--cover { top: 105px; background: #5d6b78; }
  .slide--about { top: 729px; }
  .slide--services { top: 1353px; }
  .slide--gallery { top: 1977px; background: var(--navy); }
  .slide--chart { top: 2600px; }

  .photo { position: absolute; }

  .brand { position: absolute; display: flex; align-items: center; gap: 10px; font-family: 'Roboto', Arial, sans-serif; font-weight: 400; font-size: 20px; letter-spacing: 1.5px; color: var(--teal); white-space: nowrap; }
  .brand__mark { width: 14px; height: 14px; background: currentColor; }
  .brand--light { color: var(--white); }

  .tag { position: absolute; left: 0; background: var(--teal); color: var(--white); }
  .tag__title { font-weight: 900; font-size: 31px; letter-spacing: 0.5px; }

  /* cover */
  .cover-tag { top: 463px; width: 370px; height: 100px; padding: 20px 0 0 28px; }
  .cover-tag__kicker { font-size: 19px; font-weight: 300; letter-spacing: 0.5px; }
  .cover-tag__title { font-size: 29px; font-weight: 900; margin-top: 4px; }

  /* about */
  .about-text { position: absolute; left: 44px; top: 68px; width: 310px; font-size: 13.6px; line-height: 21px; color: var(--ink-soft); }
  .section-tag { top: 475px; width: 230px; height: 88px; padding: 30px 0 0 33px; }

  /* services */
  .card { position: absolute; top: 42px; width: 295px; height: 386px; background: var(--card-bg); }
  .card__photo { position: absolute; left: 0; top: 0; width: 295px; height: 176px; }
  .card__title { position: absolute; left: 26px; top: 209px; font-size: 13.4px; font-weight: 400; color: var(--ink); white-space: nowrap; }
  .card__text { position: absolute; left: 26px; top: 242px; width: 240px; font-size: 12.3px; line-height: 17.5px; color: var(--ink-soft); }

  /* gallery */
  .gallery-title { position: absolute; left: 628px; top: 70px; width: 300px; font-size: 22px; font-weight: 700; line-height: 34px; color: var(--white); }
  .gallery-text { position: absolute; left: 628px; top: 156px; width: 295px; font-size: 14.6px; line-height: 21px; color: var(--white); font-weight: 300; }

  /* chart */
  .chart-title { position: absolute; left: 44px; top: 28px; width: 440px; font-size: 26px; line-height: 37px; font-weight: 400; color: var(--navy); }
  .chart-rule { position: absolute; left: 44px; top: 123px; width: 928px; height: 2px; background: var(--rule); }
  .chart { position: absolute; left: 21px; top: 210px; }
  .chart-notes { position: absolute; left: 571px; top: 176px; width: 385px; font-size: 13.6px; line-height: 22px; color: var(--ink-soft); }
  .chart-notes p + p { margin-top: 23px; }
</style>
</head>
<body>

  <section class="slide slide--cover">
    <div class="photo" role="img" aria-label="Business team meeting around a conference table in a bright office with tall windows" style="left:0;top:0;width:1002px;height:563px;background:linear-gradient(100deg,#c8d1d8 0%,#8a96a1 35%,#5b5f63 60%,#b9c5cf 100%);"></div>
    <div class="brand" style="left:400px;top:92px;color:var(--navy);"><span class="brand__mark" style="background:var(--teal);"></span>Aurelien Morvan</div>
    <div class="tag cover-tag">
      <div class="cover-tag__kicker">WELCOME TO</div>
      <div class="cover-tag__title">AURELIEN MORVAN</div>
    </div>
  </section>

  <section class="slide slide--about">
    <p class="about-text">There are many variations of passages of Lorem Ipsum available, but the majority have suffered alteration in some form, by injected humour, or randomised words which don't look even slightly believable. If you are going to use a passage of Lorem Ipsum, you need to be sure there isn't anything embarrassing hidden in the middle of text. All the Lorem Ipsum generators on the Internet tend to repeat predefined chunks as necessary, making this the first true generator on the Internet. It uses a dictionary of over 200 Latin words, combined with a handful of model sentence structures, to generate Lorem Ipsum which looks reasonable. The generated Lorem Ipsum is therefore always free from repetition, injected humour, or non-characteristic words etc.</p>
    <div class="photo" role="img" aria-label="Colleagues in discussion at a meeting table in a bright office" style="left:402px;top:43px;width:564px;height:383px;background:linear-gradient(110deg,#e6eaee 0%,#a9b4bf 45%,#7d8b99 70%,#dfe4e8 100%);"></div>
    <div class="tag section-tag"><span class="tag__title">ABOUT US</span></div>
    <div class="brand" style="left:782px;top:500px;"><span class="brand__mark"></span>Aurelien Morvan</div>
  </section>

  <section class="slide slide--services">
    <article class="card" style="left:31px;">
      <div class="card__photo" role="img" aria-label="Two business people shaking hands in front of a large office window" style="background:linear-gradient(180deg,#5c7f9e 0%,#c9d6e0 55%,#4a5560 100%);"></div>
      <h3 class="card__title">LOREM IPSUM IS SIMPLY DUMMY TEXT</h3>
      <p class="card__text">There are many variations of passages of Lorem Ipsum available, but the majority have suffered alteration in some form, by injected humour, or randomised words which don't look even slightly believable. If you are going to use a.</p>
    </article>
    <article class="card" style="left:352px;">
      <div class="card__photo" role="img" aria-label="Hands over a desk covered with printed charts, a calculator and a phone" style="background:linear-gradient(135deg,#f1f3f5 0%,#dfe5ea 60%,#c3ccd4 100%);"></div>
      <h3 class="card__title">LOREM IPSUM IS SIMPLY DUMMY TEXT</h3>
      <p class="card__text">There are many variations of passages of Lorem Ipsum available, but the majority have suffered alteration in some form, by injected humour, or randomised words which don't look even slightly believable. If you are going to use a.</p>
    </article>
    <article class="card" style="left:675px;">
      <div class="card__photo" role="img" aria-label="Digital business growth concept with glowing technology icons on dark blue" style="background:radial-gradient(circle at 55% 55%,#3fa7c9 0%,#164a78 40%,#0a1a33 100%);"></div>
      <h3 class="card__title">LOREM IPSUM IS SIMPLY DUMMY TEXT</h3>
      <p class="card__text">There are many variations of passages of Lorem Ipsum available, but the majority have suffered alteration in some form, by injected humour, or randomised words which don't look even slightly believable. If you are going to use a.</p>
    </article>
    <div class="tag section-tag"><span class="tag__title">SERVICES</span></div>
    <div class="brand" style="left:782px;top:500px;"><span class="brand__mark"></span>Aurelien Morvan</div>
  </section>

  <section class="slide slide--gallery">
    <div class="photo" role="img" aria-label="Consultant presenting to a small group in a bright office" style="left:21px;top:27px;width:268px;height:287px;background:linear-gradient(160deg,#e4e7ea 0%,#b7bec5 50%,#4b4f56 100%);"></div>
    <div class="photo" role="img" aria-label="Businessman overlaid with city skyline and financial chart at sunset" style="left:302px;top:27px;width:268px;height:287px;background:linear-gradient(170deg,#cfd7de 0%,#5b6d80 45%,#e0a050 75%,#3a2a22 100%);"></div>
    <div class="photo" role="img" aria-label="Team meeting around a table beside a flip chart" style="left:21px;top:327px;width:268px;height:217px;background:linear-gradient(150deg,#eef1f3 0%,#bcc6cf 50%,#6f7d8a 100%);"></div>
    <div class="photo" role="img" aria-label="Top view of colleagues working with laptops and tablets at a desk" style="left:302px;top:327px;width:268px;height:217px;background:linear-gradient(140deg,#f0f1f2 0%,#a6adb4 50%,#3c4148 100%);"></div>
    <h2 class="gallery-title">Lorem Ipsum is simply dummy text of the printing</h2>
    <p class="gallery-text">There are many variations of passages of Lorem Ipsum available, but the majority have suffered alteration in some form, by injected humour, or randomised words which don't look even slightly believable. If you are going to use a passage of Lorem Ipsum, you need to be sure there isn't anything embarrassing hidden in the middle of text. All the Lorem Ipsum generators on the Internet tend to repeat predefined chunks as necessary, making this the first true generator</p>
    <div class="brand brand--light" style="left:772px;top:470px;"><span class="brand__mark"></span>Aurelien Morvan</div>
  </section>

  <section class="slide slide--chart">
    <h2 class="chart-title">Lorem Ipsum is simply dummy text of the printing and typesetting</h2>
    <div class="chart-rule"></div>
    <svg class="chart" width="520" height="315" viewBox="0 0 520 315" font-family="Roboto, Arial, sans-serif">
      <g font-size="9" fill="#333">
        <text x="0" y="18">800</text><text x="0" y="52">700</text><text x="0" y="86">600</text>
        <text x="0" y="120">500</text><text x="0" y="153">400</text><text x="0" y="187">300</text>
        <text x="0" y="221">200</text><text x="0" y="255">100</text><text x="4" y="289">0</text>
      </g>
      <g>
        <rect x="37" y="266" width="24" height="29" fill="#177f8c"/>
        <rect x="70" y="251" width="24" height="44" fill="#0b2238"/>
        <rect x="104" y="239" width="24" height="56" fill="#177f8c"/>
        <rect x="137" y="226" width="24" height="69" fill="#0b2238"/>
        <rect x="171" y="185" width="24" height="110" fill="#177f8c"/>
        <rect x="204" y="151" width="24" height="144" fill="#0b2238"/>
        <rect x="237" y="75" width="24" height="220" fill="#0b2238"/>
        <rect x="271" y="151" width="24" height="144" fill="#177f8c"/>
        <rect x="304" y="161" width="24" height="134" fill="#0b2238"/>
        <rect x="338" y="178" width="24" height="117" fill="#177f8c"/>
        <rect x="371" y="197" width="24" height="98" fill="#0b2238"/>
        <rect x="404" y="170" width="24" height="125" fill="#177f8c"/>
        <rect x="438" y="221" width="24" height="74" fill="#0b2238"/>
        <rect x="471" y="244" width="24" height="51" fill="#177f8c"/>
      </g>
      <g font-size="6.5" fill="#333" text-anchor="middle">
        <text x="49" y="309">151,616</text><text x="82" y="309">161,171</text><text x="116" y="309">171,181</text>
        <text x="149" y="309">181,191</text><text x="183" y="309">191,201</text><text x="216" y="309">201,211</text>
        <text x="249" y="309">211,221</text><text x="283" y="309">221,231</text><text x="316" y="309">231,241</text>
        <text x="350" y="309">241,251</text><text x="383" y="309">251,261</text><text x="416" y="309">261,271</text>
        <text x="450" y="309">271,281</text><text x="483" y="309">281,291</text>
      </g>
    </svg>
    <div class="chart-notes">
      <p>Contrary to popular belief, Lorem Ipsum is not simply random text. It has roots in a piece of classical Latin literature from 45 BC, making it over 2000 years old. Julien Marchetti, a Latin professor at Saint-Aubin College</p>
      <p>There are many variations of passages of Lorem Ipsum available, but the majority have suffered alteration in some form, by injected humour, or randomised words which don't look even slightly believable.</p>
      <p>Lorem Ipsum is simply dummy text of the printing and typesetting industry. Lorem Ipsum has been the industry's standard.</p>
    </div>
    <div class="brand" style="left:782px;top:500px;"><span class="brand__mark"></span>Aurelien Morvan</div>
  </section>

</body>
</html>
```